mental health business card

Double sided business card with logo on front and practitioners details on back.
The front of card should be while and back either blue or grey to match logo.

Space on back for appointment date and time to be written.

Please note that details are not available yet for address etc as currently moving 4500km across Australia. Just use generic or old info from attached letterhead.
Updates

Dear Designers,

Please note business card is also appointment card must have area where  date and time of clients next appointment can be written in.

Target Market(s)

This is card for patients and colleagues

Industry/Entity Type

Mental Health

Requirements
Must have
• Name
Director / Clinical Psychologist
email
web
phone
phone

Nice to have
• embossing on front of card

```html
<!DOCTYPE html>
<html lang="en">
<head>
<meta charset="utf-8">
<title>Clearview Wellbeing – Business Card</title>
<link href="https://fonts.googleapis.com/css2?family=Lato:wght@300;400;700;900&display=swap" rel="stylesheet">
<style>
  :root {
    --page-bg: #e9e7e4;
    --card-white: #ffffff;
    --brand-grey: #8a8b8d;
    --brand-grey-light: #a4a5a7;
    --brand-teal: #138fb0;
    --brand-navy: #14285a;
    --ink-dark: #2c2d2f;
    --ink-white: #ffffff;
  }
  * { box-sizing: border-box; margin: 0; padding: 0; }
  html, body { width: 1200px; height: 800px; overflow: hidden; }
  body {
    background: var(--page-bg);
    font-family: "Lato", sans-serif;
    position: relative;
  }
  .card {
    position: absolute;
    top: 250px;
    width: 525px;
    height: 300px;
    overflow: hidden;
    box-shadow: 0 6px 18px rgba(0,0,0,0.18);
  }
  .card--front { left: 45px; background: var(--card-white); }
  .card--back {
    left: 630px;
    background: linear-gradient(120deg, var(--brand-teal) 0%, #1a6f9a 45%, var(--brand-navy) 100%);
  }

  /* Front face */
  .front__brand {
    position: absolute; left: 110px; top: 48px;
    display: flex; align-items: center; gap: 14px;
  }
  .brand-square {
    width: 52px; height: 52px; border-radius: 5px;
    background: linear-gradient(135deg, var(--brand-teal), var(--brand-navy));
  }
  .brand-name {
    font-weight: 300; color: var(--brand-navy);
    font-size: 30px; line-height: 1; letter-spacing: 1px; text-transform: uppercase;
  }
  .brand-name span { display: block; font-size: 15px; letter-spacing: 3px; margin-top: 4px; }
  .front__role {
    position: absolute; right: 34px; top: 104px; text-align: center;
    color: var(--ink-dark);
  }
  .front__role-title { font-weight: 900; font-size: 19px; letter-spacing: 0.5px; line-height: 1.1; }
  .front__role-sub { font-weight: 700; font-size: 8px; letter-spacing: 0.3px; text-transform: uppercase; margin-top: 2px; }

  .front__grey-band {
    position: absolute; left: 0; right: 0; top: 150px; bottom: 0;
    background: var(--brand-grey);
  }
  .front__blue-band {
    position: absolute; left: 0; right: 0; top: 164px; height: 100px;
    background: linear-gradient(100deg, var(--brand-teal) 0%, #156b92 60%, var(--brand-navy) 100%);
    border-bottom: 3px solid var(--card-white);
  }
  .front__mark-box {
    position: absolute; left: 20px; top: 118px; width: 62px; height: 62px;
    background: var(--brand-grey-light); border: 3px solid var(--card-white);
    display: flex; align-items: center; justify-content: center;
  }
  .front__mark-box .brand-square { width: 40px; height: 40px; }
  .contact-list {
    position: absolute; left: 100px; top: 176px; list-style: none;
    color: var(--ink-white); font-size: 10.5px; line-height: 19px;
  }
  .contact-list li { display: flex; align-items: center; gap: 8px; }
  .contact-list svg { width: 10px; height: 10px; fill: var(--ink-white); }

  /* Back face */
  .back__brand {
    position: absolute; left: 90px; top: 64px;
    display: flex; align-items: center; gap: 16px;
  }
  .back__brand .brand-square { background: var(--card-white); width: 66px; height: 66px; }
  .back__brand .brand-name { color: var(--ink-white); font-size: 36px; }
  .back__brand .brand-name span { font-size: 17px; }
  .back__role-band {
    position: absolute; left: 0; right: 0; bottom: 0; height: 70px;
    background: var(--brand-grey);
    display: flex; align-items: center; justify-content: space-between;
    padding: 0 26px;
    color: var(--ink-white);
  }
  .appointment { display: flex; flex-direction: column; gap: 8px; }
  .appointment__label {
    font-weight: 700; font-size: 9px; letter-spacing: 1px; text-transform: uppercase;
  }
  .appointment__fields { display: flex; gap: 14px; font-size: 11px; }
  .appointment__field { display: flex; align-items: flex-end; gap: 6px; }
  .appointment__line {
    display: inline-block; height: 1px; background: var(--ink-white);
    margin-bottom: 2px;
  }
  .appointment__line--date { width: 90px; }
  .appointment__line--time { width: 60px; }
  .back__role { font-weight: 700; font-size: 13px; }
</style>
</head>
<body>
  <section class="card card--front" aria-label="Card front">
    <div class="front__brand">
      <div class="brand-square"></div>
      <div class="brand-name">Clearview<span>Wellbeing</span></div>
    </div>
    <div class="front__role">
      <div class="front__role-title">DIRECTOR</div>
      <div class="front__role-sub">Clinical Psychologist</div>
    </div>
    <div class="front__grey-band"></div>
    <div class="front__blue-band"></div>
    <div class="front__mark-box"><div class="brand-square"></div></div>
    <ul class="contact-list">
      <li><svg viewBox="0 0 10 10"><path d="M2 0h2l1 2.5-1.3 1a5 5 0 0 0 2.8 2.8l1-1.3L10 6v2a2 2 0 0 1-2 2A8 8 0 0 1 0 2a2 2 0 0 1 2-2z"/></svg>+(000) 000 0000</li>
      <li><svg viewBox="0 0 10 10"><path d="M2 0h6v3H2zM0 4h10v4H8v2H2V8H0z"/></svg>+(000) 000 0000</li>
      <li><svg viewBox="0 0 10 10"><path d="M0 2h10v6H0z M0 2l5 3.5L10 2" stroke="#138fb0" stroke-width="0.8"/></svg>hello@clearviewwellbeing.com</li>
      <li><svg viewBox="0 0 10 10"><circle cx="5" cy="5" r="4.5"/></svg>www.clearviewwellbeing.com</li>
    </ul>
  </section>

  <section class="card card--back" aria-label="Card back">
    <div class="back__brand">
      <div class="brand-square"></div>
      <div class="brand-name">Clearview<span>Wellbeing</span></div>
    </div>
    <div class="back__role-band">
      <div class="appointment">
        <div class="appointment__label">Next appointment</div>
        <div class="appointment__fields">
          <span class="appointment__field">Date <span class="appointment__line appointment__line--date"></span></span>
          <span class="appointment__field">Time <span class="appointment__line appointment__line--time"></span></span>
        </div>
      </div>
      <div class="back__role">Director / Clinical Psychologist</div>
    </div>
  </section>
</body>
</html>
```